Website for Wedding Cake Business based in Suffolk countryside

I need a website to advertise my services. I bake wedding cakes and celebration cakes. My style of baking is very rustic and I use lots of local and homegrown ingredients within my baking. I’d like the website to be classy but countryside chic. I want to website to reflect quality and sophistication but also keep the countryside vibe. My logo is currently a mustard yellow and grey but this may be changed so the colour palette is completely open.

Target Market(s)

Couples and women aged 21-40

Industry/Entity Type

Wedding

Number of Pages Required

4 page

Colors

Designer to choose colors to be used in the design.

Requirements
Must have
• Must appeal to men and women. Must have a contact button, social media links, price list and photo gallery.
• Functioning drop downs (price list, gallery, booking form)
Nice to have
• Very simple layout with menu bar across the top of the page. A section can update which shows which feeding Faye or show I’ll be a next with a map.
Should not have
• Nothing to bold, block coloured or cheesy.

```html
<!DOCTYPE html>
<html lang="en">
<head>
<meta charset="utf-8">
<title>Hazelbrook — Wedding &amp; Celebration Cakes</title>
<link rel="stylesheet" href="https://fonts.googleapis.com/css2?family=Courgette&family=Cedarville+Cursive&family=Open+Sans:wght@400;600;700&family=Montserrat:wght@400;600;700&display=swap">
<style>
:root{
  --ink:#2e2a28;
  --text:#8a8582;
  --dark:#2b2b2b;
  --night:#1f1c1b;
  --coral:#f07a6a;
  --pink:#f06b7d;
  --sage:#a3b07a;
  --mustard:#d4c13a;
  --orange:#f6a366;
  --price:#f2994a;
  --cream:#fdf0c8;
  --rust:#c0641f;
  --plum:#a8589a;
  --line:#ececec;
  --white:#fff;
}
*{box-sizing:border-box;margin:0;padding:0}
html,body{width:1200px;height:3482px;overflow:hidden}
body{position:relative;background:var(--white);font-family:"Open Sans",sans-serif;color:var(--text)}
.abs{position:absolute}
.script{font-family:"Courgette",cursive;color:var(--ink);font-weight:400}
.rule{width:90px;height:4px;background:var(--coral);margin:0 auto}
.btn{display:flex;align-items:center;justify-content:center;color:var(--white);font-family:"Montserrat",sans-serif;font-size:13px;font-weight:600;letter-spacing:1px;text-transform:uppercase}

/* top bar */
.topbar{left:0;top:0;width:1200px;height:32px;background:var(--dark);color:#cfcfcf;font-size:12px;display:flex;align-items:center;padding:0 50px;gap:30px}
.topbar .right{margin-left:auto;display:flex;gap:26px}
.topbar span{display:flex;align-items:center;gap:7px}

/* header */
.header{left:0;top:32px;width:1200px;height:108px}
.brand{left:46px;top:18px;width:121px;height:78px;display:flex;align-items:center;gap:8px;flex-direction:column;justify-content:center}
.brand-mark{width:22px;height:22px;background:var(--rust)}
.brand-name{font-family:"Montserrat",sans-serif;font-weight:700;font-size:19px;color:var(--rust);letter-spacing:1px}
.brand-tag{font-size:8px;color:var(--ink);margin-top:-6px}
.nav{top:48px;font-family:"Montserrat",sans-serif;font-size:14px;font-weight:600;letter-spacing:1px;color:var(--ink)}
.nav.active{color:var(--plum)}
.cart-badge{left:1113px;top:34px;width:32px;height:32px;border-radius:50%;background:var(--coral);display:flex;align-items:center;justify-content:center}
.cart-count{left:1134px;top:28px;width:16px;height:16px;border-radius:50%;background:var(--dark);color:#fff;font-size:10px;text-align:center;line-height:16px}

/* hero */
.hero{left:0;top:140px;width:1200px;height:552px;background:radial-gradient(circle at 30% 40%,#f6a07a 0,#f9d6c8 18%,transparent 30%),radial-gradient(circle at 70% 35%,#f5906a 0,#f8cdbc 16%,transparent 28%),linear-gradient(180deg,#dfe6e7 0%,#f1eded 40%,#c8d89a 75%,#9fb3d8 100%)}
.wave{left:0;width:1200px;height:24px}

/* about */
.about-photo{left:46px;top:800px;width:544px;height:398px;background:linear-gradient(135deg,#8a5c45,#d49a63 45%,#6b3f33 100%)}
.about-box{left:543px;top:824px;width:578px;height:344px;background:#fff;box-shadow:0 2px 14px rgba(0,0,0,.15);text-align:center;padding:40px 60px 0}
.about-box h2{font-family:"Cedarville Cursive",cursive;font-size:44px;color:var(--ink);font-weight:400}
.about-box p{font-size:14px;line-height:28px;margin-top:16px}
.about-box .btn{width:158px;height:47px;margin:36px auto 0;background:var(--coral);font-family:"Courgette",cursive;font-weight:400;font-size:16px;letter-spacing:2px}

/* wedding cake band */
.band{left:0;top:1311px;width:1200px;height:419px;background:linear-gradient(180deg,#2a2522,var(--night) 60%,#151312)}
.band-title{left:0;top:1335px;width:1200px;text-align:center;color:#fff}
.band-title h2{font-family:"Courgette",cursive;font-size:50px;font-weight:400}
.band-title .rule{margin-top:14px}
.band-title p{font-size:14px;line-height:29px;width:760px;margin:20px auto 0;color:#f0ece9}

.card{top:1583px;width:340px;height:583px;background:#fff;box-shadow:0 2px 12px rgba(0,0,0,.12);text-align:center;padding-top:36px}
.card h3{font-family:"Courgette",cursive;font-size:30px;color:#1e1b1a;font-weight:400}
.card .photo{width:214px;height:214px;border-radius:50%;margin:30px auto 0}
.card p{font-size:13px;line-height:26px;width:240px;margin:32px auto 0}
.card .btn{width:185px;height:40px;border-radius:20px;margin:30px auto 0}

/* products */
.intro{left:0;top:2265px;width:1200px;text-align:center}
.intro h2{font-family:"Cedarville Cursive",cursive;font-size:42px;color:var(--ink);font-weight:400}
.intro .rule{margin-top:10px}
.intro p{font-size:14px;line-height:29px;width:760px;margin:18px auto 0}
.product{top:2488px;width:254px;height:428px;background:#f9f9f9;border:1px solid var(--line);text-align:center}
.product .photo{height:256px;position:relative}
.price{position:absolute;left:18px;top:18px;width:86px;height:82px;background:rgba(60,45,40,.85);color:#fff;font-family:"Courgette",cursive;font-size:20px;display:flex;align-items:center;justify-content:center}
.product h4{font-size:16px;font-weight:400;color:var(--price);margin-top:22px}
.product h4 span{color:var(--ink)}
.product .cat{font-size:12px;margin-top:8px;padding-bottom:26px;border-bottom:1px solid var(--line)}
.product .actions{display:flex;justify-content:center;gap:10px;margin-top:20px}
.product .actions .btn{width:102px;height:35px;background:var(--orange);font-family:"Open Sans",sans-serif;font-size:11px;letter-spacing:0;text-transform:none;border-radius:2px}

/* features */
.feature{top:3001px;width:352px;height:86px;background:var(--cream);display:flex;align-items:center;gap:18px;padding-left:32px}
.feature strong{display:block;font-family:"Montserrat",sans-serif;font-size:15px;color:var(--ink)}
.feature small{font-size:12px;color:#555}

/* footer */
.footer{left:0;top:3133px;width:1200px;height:307px;background:var(--dark);color:#d6d6d6}
.footer h5{font-family:"Montserrat",sans-serif;font-size:17px;color:#fff;letter-spacing:.5px}
.links{left:360px;top:62px}
.links li{list-style:none;font-size:14px;line-height:31px}
.links h5{margin-bottom:18px}
.pay{left:573px;top:62px}
.pay h6{font-family:"Montserrat",sans-serif;font-size:12px;color:#fff;margin:22px 0 10px}
.badges{display:flex;gap:8px;margin-top:20px}
.badges i{display:block;width:44px;height:24px;border-radius:4px;background:#d8d8d8}
.badges.sm i{width:40px;height:18px;background:#bdbdbd}
.news{left:882px;top:62px;width:270px}
.news p{font-size:14px;line-height:25px;margin-top:16px}
.signup{display:flex;margin-top:14px}
.signup span{width:195px;height:34px;background:#fff;color:#555;font-size:11px;padding:10px 8px}
.signup b{width:56px;height:34px;background:var(--pink);display:flex;align-items:center;justify-content:center}
.social{display:flex;gap:16px;margin-top:20px}
.social i{width:11px;height:11px;border-radius:50%;background:#8d8d8d;display:block}
.bottom{left:0;top:3440px;width:1200px;height:42px;background:var(--rust);color:#fff;font-size:12px;display:flex;align-items:center;padding:0 60px}
.bottom nav{margin-left:auto;display:flex;gap:26px}
</style>
</head>
<body>

<div class="abs topbar">
  <span><svg width="12" height="12" viewBox="0 0 24 24" fill="#cfcfcf"><path d="M6.6 10.8a15 15 0 006.6 6.6l2.2-2.2c.3-.3.7-.4 1-.2 1.1.4 2.3.6 3.6.6.6 0 1 .4 1 1V20c0 .6-.4 1-1 1A17 17 0 013 4c0-.6.4-1 1-1h3.5c.6 0 1 .4 1 1 0 1.3.2 2.5.6 3.6.1.3 0 .7-.2 1z"/></svg>01234-567-890</span>
  <span><svg width="13" height="10" viewBox="0 0 24 18" fill="#cfcfcf"><path d="M0 0h24v18H0zM2 2l10 8 10-8z" fill-rule="evenodd"/></svg>hello@hazelbrookbakes.com</span>
  <div class="right">
    <span><svg width="12" height="12" viewBox="0 0 24 24"><circle cx="12" cy="12" r="8" fill="none" stroke="#cfcfcf" stroke-width="5" stroke-dasharray="4 2.3"/></svg>Setting ▾</span>
    <span><svg width="11" height="12" viewBox="0 0 22 24" fill="#cfcfcf"><circle cx="11" cy="6" r="6"/><path d="M0 24c0-7 5-10 11-10s11 3 11 10z"/></svg>Account ▾</span>
  </div>
</div>

<header class="abs header">
  <div class="abs brand">
    <div class="brand-mark"></div>
    <div class="brand-name">HAZELBROOK</div>
    <div class="brand-tag">Cakes and Bakehouse</div>
  </div>
  <div class="abs nav active" style="left:362px">HOME</div>
  <div class="abs nav" style="left:473px">WEDDINGS</div>
  <div class="abs nav" style="left:622px">CELEBRATIONS</div>
  <div class="abs nav" style="left:802px">INFORMATION</div>
  <div class="abs nav" style="left:978px">CONTACT</div>
  <svg class="abs" style="left:1072px;top:47px" width="16" height="16" viewBox="0 0 24 24"><circle cx="10" cy="10" r="7" fill="none" stroke="#2e2a28" stroke-width="3"/><path d="M15 15l7 7" stroke="#2e2a28" stroke-width="3"/></svg>
  <div class="abs cart-badge"><svg width="16" height="14" viewBox="0 0 24 20" fill="#fff"><path d="M0 0h4l1 3h19l-3 9H7zM8 16a2 2 0 100 4 2 2 0 000-4zm11 0a2 2 0 100 4 2 2 0 000-4z"/></svg></div>
  <div class="abs cart-count">0</div>
</header>

<section class="abs hero" role="img" aria-label="Photo of cupcakes topped with swirled cream and orange sugar roses"></section>
<svg class="abs wave" style="top:140px" viewBox="0 0 1200 24" preserveAspectRatio="none"><path d="M0 0h1200v8 q-10 10-20 0 t-20 0 t-20 0 t-20 0 t-20 0 t-20 0 t-20 0 t-20 0 t-20 0 t-20 0 t-20 0 t-20 0 t-20 0 t-20 0 t-20 0 t-20 0 t-20 0 t-20 0 t-20 0 t-20 0 t-20 0 t-20 0 t-20 0 t-20 0 t-20 0 t-20 0 t-20 0 t-20 0 t-20 0 t-20 0 t-20 0 t-20 0 t-20 0 t-20 0 t-20 0 t-20 0 t-20 0 t-20 0 t-20 0 t-20 0 t-20 0 t-20 0 t-20 0 t-20 0 t-20 0 t-20 0 t-20 0 t-20 0 t-20 0 t-20 0 t-20 0 t-20 0 t-20 0 t-20 0 t-20 0 t-20 0 t-20 0 t-20 0 t-20 0 t-20 0z" fill="#fff"/></svg>
<svg class="abs wave" style="top:668px" viewBox="0 0 1200 24" preserveAspectRatio="none"><path d="M0 24h1200v-8 q-10-10-20 0 t-20 0 t-20 0 t-20 0 t-20 0 t-20 0 t-20 0 t-20 0 t-20 0 t-20 0 t-20 0 t-20 0 t-20 0 t-20 0 t-20 0 t-20 0 t-20 0 t-20 0 t-20 0 t-20 0 t-20 0 t-20 0 t-20 0 t-20 0 t-20 0 t-20 0 t-20 0 t-20 0 t-20 0 t-20 0 t-20 0 t-20 0 t-20 0 t-20 0 t-20 0 t-20 0 t-20 0 t-20 0 t-20 0 t-20 0 t-20 0 t-20 0 t-20 0 t-20 0 t-20 0 t-20 0 t-20 0 t-20 0 t-20 0 t-20 0 t-20 0 t-20 0 t-20 0 t-20 0 t-20 0 t-20 0 t-20 0 t-20 0 t-20 0 t-20 0z" fill="#fff"/></svg>

<section>
  <div class="abs about-photo" role="img" aria-label="Photo of a platter of breads, pastries and a bundt cake"></div>
  <div class="abs about-box">
    <h2>Made with love</h2>
    <p>Special cloth alert, cut from a special cloth. Let's see what Chef Rowan got that they don't want us to eat. Bless up. I'm up to something. The weather is amazing, walk with me through the pathway of more success. Take this journey with me!</p>
    <div class="btn">GO TO SHOP</div>
  </div>
</section>

<section>
  <div class="abs band" role="img" aria-label="Dark background photo of a rustic bakery table"></div>
  <div class="abs band-title">
    <h2>Wedding Cake</h2>
    <div class="rule"></div>
    <p>Special cloth alert, cut from a special cloth. Let's see what Chef Rowan got that they don't want us to eat. Bless up. I'm up to something. The weather is amazing, walk with me through the pathway of more success. Take this journey with me!</p>
  </div>
  <article class="abs card" style="left:63px">
    <h3>We Bake Breads</h3>
    <div class="photo" role="img" aria-label="Photo of sliced loaves of bread" style="background:radial-gradient(circle,#d9a05a,#8a5426)"></div>
    <p>Lorem Marlow Ipsum is a major key to success. You see the hedges, how I got it shaped up? It's important to shape up your hedges.</p>
    <div class="btn" style="background:var(--sage)">GO TO SHOP</div>
  </article>
  <article class="abs card" style="left:430px">
    <h3>Baked Patisserie</h3>
    <div class="photo" role="img" aria-label="Photo of a layered cream pastry with raspberries" style="background:radial-gradient(circle,#f3d9a8,#c98a4e 60%,#e8e2da)"></div>
    <p>Nemo enim ipsam voluptatem quia tyvoluptas sit aspernatur aut odit aut fugit, sed quia consequuntur magni dolores eos qui.</p>
    <div class="btn" style="background:var(--pink)">GO TO SHOP</div>
  </article>
  <article class="abs card" style="left:798px">
    <h3>Special Cakes</h3>
    <div class="photo" role="img" aria-label="Photo of a tiered pink celebration cake" style="background:radial-gradient(circle,#f7c6d2,#e58aa4 60%,#b9d4d6)"></div>
    <p>Nam libero tempore, cum soluta nobis est eligendi optio cumque nihil impedit quo minus id quod maxime placeat facere possimus.</p>
    <div class="btn" style="background:var(--mustard)">GO TO SHOP</div>
  </article>
</section>

<section>
  <div class="abs intro">
    <h2>Hello, We Provide Amazing Cakes</h2>
    <div class="rule"></div>
    <p>Special cloth alert, cut from a special cloth. Let's see what Chef Rowan got that they don't want us to eat. Bless up. I'm up to something. The weather is amazing, walk with me through the pathway of more success. Take this journey with me!</p>
  </div>
  <article class="abs product" style="left:46px">
    <div class="photo" role="img" aria-label="Photo of buccellato cake with cream and berries" style="background:linear-gradient(160deg,#5a1f1c,#a8453a 55%,#e9ddd0)"><div class="price">£10.00</div></div>
    <h4>Buccellato Cake</h4><div class="cat">Desserts</div>
    <div class="actions"><div class="btn">Add to cart</div><div class="btn">Add to Wishlist</div></div>
  </article>
  <article class="abs product" style="left:332px">
    <div class="photo" role="img" aria-label="Photo of bacca di montagna biscuits" style="background:linear-gradient(160deg,#2a1a12,#a4492a 55%,#c9703f)"><div class="price">£5.00</div></div>
    <h4>Bacca di montagna <span>(Sale)</span></h4><div class="cat">Apple, Desserts</div>
    <div class="actions"><div class="btn">Add to cart</div><div class="btn">Add to Wishlist</div></div>
  </article>
  <article class="abs product" style="left:617px">
    <div class="photo" role="img" aria-label="Photo of croissant muffins in a tray" style="background:linear-gradient(160deg,#4a3526,#c99763 55%,#e7c58e)"><div class="price">£1.00</div></div>
    <h4>Bacca Croissant <span>(Sale)</span></h4><div class="cat">Desserts</div>
    <div class="actions"><div class="btn">Add to cart</div><div class="btn">Add to Wishlist</div></div>
  </article>
  <article class="abs product" style="left:900px">
    <div class="photo" role="img" aria-label="Photo of golden croissants" style="background:linear-gradient(160deg,#e8dccb,#d2a878 55%,#8a6a4c)"><div class="price">£9.00</div></div>
    <h4>Croissant</h4><div class="cat">Apple, Desserts</div>
    <div class="actions"><div class="btn">Add to cart</div><div class="btn">Add to Wishlist</div></div>
  </article>
</section>

<section>
  <div class="abs feature" style="left:63px">
    <svg width="34" height="34" viewBox="0 0 24 24" fill="#2e2a28"><path d="M21 16v-2l-8-5V3.5a1.5 1.5 0 00-3 0V9l-8 5v2l8-2.5V19l-2 1.5V22l3.5-1 3.5 1v-1.5L13 19v-5.5z"/></svg>
    <div><strong>FREE SHIPPING WORLDWIDE</strong><small>On All Orders Of USD 250,00+</small></div>
  </div>
  <div class="abs feature" style="left:425px">
    <svg width="34" height="34" viewBox="0 0 24 24" fill="none" stroke="#2e2a28" stroke-width="1.8"><path d="M4 14v-2a8 8 0 0116 0v2"/><rect x="3" y="13" width="4" height="6" rx="1"/><rect x="17" y="13" width="4" height="6" rx="1"/></svg>
    <div><strong>24/7 CUSTOMER SERVICE</strong><small>Get Help When You Need It.</small></div>
  </div>
  <div class="abs feature" style="left:789px">
    <svg width="34" height="34" viewBox="0 0 24 24" fill="none" stroke="#2e2a28" stroke-width="2"><path d="M20 12a8 8 0 11-2.3-5.6"/><path d="M20 3v5h-5"/></svg>
    <div><strong>100% MONEY BACK</strong><small>30 Day Money Back Guarantee.</small></div>
  </div>
</section>

<footer class="abs footer">
  <div class="abs links">
    <h5>QUICK LINKS</h5>
    <ul><li>About Us</li><li>Privacy Policy</li><li>Terms &amp; Condition</li><li>Best Seller</li><li>Manufactures</li></ul>
  </div>
  <div class="abs pay">
    <h5>PAYMENT METHODS</h5>
    <div class="badges"><i></i><i></i><i></i><i></i></div>
    <h6>SHIPPING PARTNER</h6>
    <div class="badges sm"><i></i><i></i><i></i></div>
    <div class="badges sm" style="margin-top:10px"><i></i><i></i><i></i></div>
  </div>
  <div class="abs news">
    <h5>NEWSLETTER !</h5>
    <p>Sign up for our newsletter and get 15% off your next order.</p>
    <div class="signup"><span>Enter your email here*</span><b><svg width="16" height="4"><rect width="16" height="3" fill="#fff"/></svg></b></div>
    <div class="social"><i></i><i></i><i></i><i></i><i></i></div>
  </div>
</footer>
<div class="abs bottom">
  <span>© 2016 Copyright Meadow Oven .All Right Reserved.</span>
  <nav><span>Privacy &amp; Cookies</span><span>Terms &amp; Conditions</span><span>Accessibility</span><span>Store Directory</span><span>About Us</span></nav>
</div>

</body>
</html>
```